Sustainable focused startup needs mobile app design for building the new economy, 3D style

For our sustainability-focused job-matching app, we want a design with a modern look and a compelling story-driven approach that appeals to the youngest professional generation and the sustainable focused companies.

Main style should reflect a 3D setup > see attached generated examples.

What we would like to see in the designs:
1. Fullscreen Visual Welcome
"Discover Your Sustainable Career Path & Make an Impact!"
2. Interactive Scroll or Tap Elements
Brief Explanation: As users scroll or tap, they’re taken through a brief introduction, like a journey:
Screen 1 - "Our Mission": “We connect young professionals with purposeful work in sustainable companies.”
Screen 2 - "Your Journey": “Explore opportunities, grow personally, and be part of a community focused on sustainability.”
Screen 3 - "Get Started": Clear CTA buttons like "Create Your Profile" or "Explore Companies."
3. Peek at the Community
that shows real young professionals with tags of their sustainability archetypes—e.g., “The Ecological Guardian” or “The Social Connector.”
Main CTA Button: "Start Now" or "Create My Profile", highlighted to guide users to registration.
4. Profile screen as seen by user
Showing drive, ambitions, skills and community membership and updates
5. Profile screen as seen by others from community perspective, inviting others to connect
6. Company profile screen, triggering users to engage

If possible, visually Engaging Icons and Graphics
Iconography: Icons representing the app's alignment with recognized sustainability efforts.
Graphics: Small animations or illustrations showing professional profiles aligning with values or impact-oriented stories to make the experience feel dynamic and rewarding.

Company website: brightorchard.net (should potentially be rebranded to reflect 3D style also!)
Note: branding pdf focuses on red and black. Please use artist freedom to add or change colours if logical.

Target Market(s)

Young Professionals

Industry/Entity Type

Sustainable recruitment

Requirements
Must have
• Profile screens

```html
<!DOCTYPE html>
<html lang="en">
<head>
<meta charset="utf-8">
<title>BrightOrchard — Web &amp; App Screens</title>
<link rel="stylesheet" href="https://fonts.googleapis.com/css2?family=Poppins:ital,wght@0,400;0,500;0,600;0,700;1,400&family=DM+Serif+Display&display=swap">
<style>
:root{
  --stage:#a9a9a9;
  --red:#d3111b;
  --deep-red:#a50c13;
  --ink:#1c1c1e;
  --muted:#6d6d72;
  --panel:#2b2b2d;
  --mist:#ebebec;
  --paper:#f6f5f5;
  --blush:#f4d6d9;
  --rose:#e7a8ae;
  --white:#ffffff;
  --line:#d9d9db;
}
*{box-sizing:border-box;margin:0;padding:0}
html,body{width:849px;height:1200px;overflow:hidden}
body{background:var(--stage);font-family:"Poppins",sans-serif;color:var(--ink);position:relative}
.abs{position:absolute}
svg.icon{width:100%;height:100%;fill:none;stroke:currentColor;stroke-width:1.6;stroke-linecap:round;stroke-linejoin:round}

/* desktop screens */
.desk{position:absolute;width:288px;height:180px;background:var(--mist);overflow:hidden;border-radius:2px;box-shadow:0 2px 8px rgba(0,0,0,.18)}
.brand{position:absolute;display:flex;align-items:center;gap:2px;font-weight:700;color:var(--ink);white-space:nowrap}
.brand .dot{border-radius:50%;background:var(--red);flex:none}
.brand.light{color:var(--white)}
.nav{position:absolute;top:15px;left:94px;display:flex;gap:8px;font-size:4px}
.nav span.on{color:var(--red);font-weight:600;border-bottom:.7px solid var(--red);padding-bottom:2px}
.auth{position:absolute;top:13px;right:16px;display:flex;gap:5px;align-items:center;font-size:3.4px}
.auth .pill{background:var(--rose);color:var(--deep-red);padding:2px 6px;border-radius:4px}
.hero-title{position:absolute;left:15px;top:48px;font-size:16.2px;line-height:.98;font-weight:500;letter-spacing:-.2px}
.hero-sub{position:absolute;left:15px;top:124px;font-size:4.6px;line-height:1.35}
.btn{position:absolute;background:var(--deep-red);color:var(--white);font-weight:600;display:flex;align-items:center;justify-content:center;border-radius:1.5px}
.pager{position:absolute;display:flex;flex-direction:column;gap:3.5px}
.pager i{width:3.2px;height:3.2px;border-radius:50%;border:.7px solid var(--red);display:block}
.pager i.on{background:var(--red)}
.art{position:absolute}
.about-copy{position:absolute;left:135px;top:35px;width:132px;font-size:3.9px;line-height:1.42}
.about-copy b{display:block;margin-top:6px;font-size:3.9px}
.about-copy em{display:block;margin-top:6px}

/* dashboard */
.side{position:absolute;left:0;top:0;width:66px;height:180px;background:var(--panel);color:#b9b9bd;font-size:4px}
.side .menu{position:absolute;left:8px;top:42px;width:50px}
.side .item{display:flex;align-items:center;gap:4px;height:10.5px;padding-left:4px;border-radius:5px}
.side .item svg{width:4px;height:4px}
.side .item.on{background:var(--red);color:var(--white);font-weight:600}
.side .rule{position:absolute;left:10px;top:125px;width:46px;height:.6px;background:#555}
.side .foot{position:absolute;left:10px;top:140px}
.main{position:absolute;left:66px;top:0;width:222px;height:180px;background:var(--paper)}
.main h2{position:absolute;left:9px;top:8px;font-size:5px;font-weight:600}
.tools{position:absolute;right:9px;top:8px;display:flex;gap:3px;color:var(--muted)}
.tools svg{width:5px;height:5px}
.card{position:absolute;border-radius:3px;background:var(--white);box-shadow:0 1px 3px rgba(0,0,0,.12);overflow:hidden}
.lbl{position:absolute;font-size:4.3px;font-weight:600}
.tiles{position:absolute;display:flex;gap:3px}
.tile{width:21px;height:20px;background:var(--white);border:.5px solid var(--line);border-radius:2px;display:flex;flex-direction:column;align-items:center;justify-content:center;gap:1.5px;font-size:1.9px;color:var(--muted);text-align:center}
.tile svg{width:10px;height:10px;color:var(--ink)}
.ctile{width:27px;height:35px;border:.6px solid var(--rose);border-radius:2px;background:var(--white);display:flex;flex-direction:column;align-items:center;justify-content:center;gap:4px;font-size:2.8px;color:var(--muted)}
.ctile svg{width:15px;height:15px;color:var(--ink)}
.tiny{font-size:2.2px;line-height:1.35;color:var(--muted)}

/* phones */
.phone{position:absolute;width:143px;height:310px;border-radius:17px;overflow:hidden;box-shadow:0 2px 8px rgba(0,0,0,.2)}
.status{position:absolute;top:6px;left:12px;right:12px;display:flex;justify-content:space-between;font-size:4.2px}
.status .sys{display:flex;gap:2px;align-items:center}
.status .sys i{display:block;background:currentColor;border-radius:.5px}
.homebar{position:absolute;bottom:6px;left:52px;width:39px;height:1.3px;border-radius:1px;background:var(--ink)}
.row{position:absolute;left:8px;width:127px;height:15px;display:flex;align-items:center;gap:5px;padding:0 5px;font-size:6px;letter-spacing:.5px;border-bottom:.5px solid var(--line)}
.row .ic{width:9px;height:9px;border:.5px solid var(--line);border-radius:2px;padding:1.2px;color:var(--muted)}
.row .chev{margin-left:auto;width:5px;height:5px}
.match{position:absolute;left:9px;width:125px;height:42px;background:var(--white);border-radius:3px;box-shadow:0 1px 3px rgba(0,0,0,.1)}
.match .pct{position:absolute;right:6px;top:6px;font-size:10px;font-weight:700;line-height:.85;text-align:right}
.match .pct small{font-size:6px;display:block}
.match .go{position:absolute;right:6px;bottom:6px;background:var(--red);color:var(--white);font-size:3.6px;font-weight:600;padding:1.5px 4px;border-radius:2px}
.match .ttl{position:absolute;left:48px;top:8px;font-size:5.4px;font-weight:600;line-height:1}
</style>
</head>
<body>

<svg width="0" height="0" style="position:absolute" aria-hidden="true">
  <defs>
    <symbol id="i-globe" viewBox="0 0 24 24"><circle cx="12" cy="12" r="9"/><ellipse cx="12" cy="12" rx="4" ry="9"/><path d="M3 12h18M5 7h14M5 17h14"/></symbol>
    <symbol id="i-leaf" viewBox="0 0 24 24"><path d="M5 19C5 10 11 5 19 5c0 8-5 14-14 14z"/><path d="M5 19l8-8"/></symbol>
    <symbol id="i-lock" viewBox="0 0 24 24"><rect x="6" y="11" width="12" height="9" rx="1.5"/><path d="M8.5 11V8a3.5 3.5 0 017 0v3"/><circle cx="12" cy="15.5" r="1"/></symbol>
    <symbol id="i-users" viewBox="0 0 24 24"><circle cx="7" cy="9" r="2.5"/><circle cx="12" cy="8" r="3"/><circle cx="17" cy="9" r="2.5"/><path d="M3 18c0-3 2-5 4-5M21 18c0-3-2-5-4-5M7 19c0-3.5 2.3-6 5-6s5 2.5 5 6z"/></symbol>
    <symbol id="i-book" viewBox="0 0 24 24"><path d="M4 17h16v3H4zM5 13h14v4H5zM4 9h16v4H4z"/><path d="M8 4l8 2-8 2z"/></symbol>
    <symbol id="i-eco" viewBox="0 0 24 24"><circle cx="12" cy="12" r="9"/><path d="M7 13h3M14 12a2 2 0 104 0 2 2 0 10-4 0M11 11a1.5 1.5 0 10.1 3"/></symbol>
    <symbol id="i-target" viewBox="0 0 24 24"><circle cx="12" cy="12" r="8"/><circle cx="12" cy="12" r="3.5"/><path d="M12 2v4M12 18v4M2 12h4M18 12h4"/></symbol>
    <symbol id="i-chev" viewBox="0 0 24 24"><path d="M9 5l7 7-7 7"/></symbol>
    <symbol id="i-back" viewBox="0 0 24 24"><path d="M15 5l-7 7 7 7"/></symbol>
    <symbol id="i-bell" viewBox="0 0 24 24"><path d="M6 17V11a6 6 0 0112 0v6l2 2H4z"/><path d="M10 21h4"/></symbol>
    <symbol id="i-chat" viewBox="0 0 24 24"><rect x="3" y="5" width="18" height="12" rx="2"/><path d="M8 17l-2 4 5-4"/></symbol>
    <symbol id="i-menu" viewBox="0 0 24 24"><path d="M4 7h16M4 12h16M4 17h16"/></symbol>
    <symbol id="i-home" viewBox="0 0 24 24"><path d="M4 11l8-7 8 7v9H4z"/><path d="M10 20v-5h4v5"/></symbol>
    <symbol id="i-user" viewBox="0 0 24 24"><circle cx="12" cy="8" r="4"/><path d="M4 21c0-4 3.5-7 8-7s8 3 8 7"/></symbol>
    <symbol id="i-heart" viewBox="0 0 24 24"><path d="M12 20S3 14 3 8.5A4.5 4.5 0 0112 6a4.5 4.5 0 019 2.5C21 14 12 20 12 20z"/></symbol>
    <symbol id="i-compass" viewBox="0 0 24 24"><circle cx="12" cy="12" r="9"/><path d="M15.5 8.5l-2 5-5 2 2-5z"/></symbol>
    <symbol id="i-search" viewBox="0 0 24 24"><circle cx="11" cy="11" r="6"/><path d="M16 16l4 4"/></symbol>
    <symbol id="i-gear" viewBox="0 0 24 24"><circle cx="12" cy="12" r="3"/><circle cx="12" cy="12" r="8"/></symbol>
    <symbol id="i-swap" viewBox="0 0 24 24"><path d="M4 8h14l-3-3M20 16H6l3 3"/></symbol>
    <symbol id="i-out" viewBox="0 0 24 24"><path d="M10 4H4v16h6M14 8l4 4-4 4M18 12H9"/></symbol>
    <symbol id="i-pencil" viewBox="0 0 24 24"><path d="M5 19l1-4L16 5l3 3L9 18z"/></symbol>
  </defs>
</svg>

<!-- ============ Web: Home ============ -->
<section class="desk" style="left:82px;top:151px" aria-label="Website home">
  <div class="brand" style="left:16px;top:14px;font-size:6px"><span class="dot" style="width:6px;height:6px"></span>BrightOrchard</div>
  <nav class="nav"><span class="on">Home</span><span>About</span><span>Services</span><span>Profile</span><span>Contact</span></nav>
  <div class="auth"><span>Login</span><span class="pill">Sign Up</span></div>
  <h1 class="hero-title">Discover Your<br>Sustainable Career<br>Path &amp; Make an<br>Impact!</h1>
  <p class="hero-sub">Join a community of changemakers<br>transforming the future.</p>
  <div class="btn" style="left:15px;top:156px;width:47px;height:12px;font-size:4px">EXPLORE</div>
  <div class="art" role="img" aria-label="3D illustration of a planet orbit system with satellite above a glowing red podium" style="left:182px;top:30px;width:98px;height:145px;border-radius:40px;background:radial-gradient(ellipse at 50% 30%,#e6d9f3 0,#c9b8e8 28%,transparent 48%),radial-gradient(ellipse at 50% 88%,#d71a22 0,#f08b87 25%,transparent 55%)"></div>
  <div class="pager" style="left:265px;top:73px"><i class="on"></i><i></i><i></i><i></i></div>
</section>

<!-- ============ Web: About ============ -->
<section class="desk" style="left:479px;top:151px" aria-label="Website about page">
  <div class="brand" style="left:16px;top:14px;font-size:6px"><span class="dot" style="width:6px;height:6px"></span>BrightOrchard</div>
  <nav class="nav" style="left:94px"><span>Home</span><span class="on">About</span><span>Services</span><span>Profile</span><span>Contact</span></nav>
  <div class="auth"><span>Login</span><span class="pill">Sign Up</span></div>
  <div class="art" role="img" aria-label="3D globe wrapped in a red geodesic network" style="left:14px;top:36px;width:115px;height:118px;border-radius:50%;background:radial-gradient(circle at 45% 42%,#f3f3f3 0,#d8d8d8 35%,#c2383a 55%,#f4c3c5 72%,transparent 73%)"></div>
  <div class="about-copy">
    At brightorchard.net, we're passionate about connecting the next generation of professionals with meaningful careers in sustainability-focused companies. Our mission is simple: to empower individuals to make an impact while pursuing personal growth and joining a community of changemakers. Through our platform, you can explore opportunities that align with your values, collaborate with like-minded peers, and contribute to a more sustainable future. Together, we're shaping a world where purpose and progress go hand in hand.
    <b>Our Mission</b>
    Connecting People with Purposeful Careers
    <em>What We Believe</em>
    Our Vision and Our Impact with short, scrollable content blocks
  </div>
  <div class="art" role="img" aria-label="Faint data network pattern" style="left:0;top:140px;width:288px;height:40px;background:linear-gradient(180deg,transparent,rgba(80,80,80,.12))"></div>
  <div class="btn" style="left:206px;top:148px;width:58px;height:11px;font-size:3.6px;background:var(--red)">LEARN MORE ABOUT US</div>
  <div class="pager" style="left:265px;top:70px"><i></i><i class="on"></i><i></i><i></i></div>
</section>

<!-- ============ Web: Profile dashboard ============ -->
<section class="desk" style="left:82px;top:403px" aria-label="Profile dashboard">
  <aside class="side">
    <div class="brand light" style="left:9px;top:15px;font-size:6px"><span class="dot" style="width:6px;height:6px"></span>BrightOrchard</div>
    <div class="menu">
      <div class="item"><svg class="icon"><use href="#i-home"/></svg>Home</div>
      <div class="item on"><svg class="icon"><use href="#i-user"/></svg>Profile</div>
      <div class="item"><svg class="icon"><use href="#i-globe"/></svg>Community Insight</div>
      <div class="item"><svg class="icon"><use href="#i-user"/></svg>Contact Us</div>
      <div class="item"><svg class="icon"><use href="#i-gear"/></svg>Settings</div>
    </div>
    <div class="rule"></div>
    <div class="foot">
      <div class="item"><svg class="icon"><use href="#i-user"/></svg>Add Account</div>
      <div class="item"><svg class="icon"><use href="#i-swap"/></svg>Switch Account</div>
      <div class="item"><svg class="icon"><use href="#i-out"/></svg>Log Out</div>
    </div>
  </aside>
  <div class="main">
    <h2>Profile</h2>
    <div class="tools"><svg class="icon"><use href="#i-chat"/></svg><svg class="icon" style="color:var(--red)"><use href="#i-bell"/></svg></div>
    <div class="card" style="left:8px;top:19px;width:92px;height:60px;background:linear-gradient(180deg,#b98b90,#f1dfe1 70%,#fff)">
      <div class="art" role="img" aria-label="Member portrait" style="left:33px;top:6px;width:27px;height:27px;border-radius:50%;background:radial-gradient(circle,#6b4a3f,#2a1d1a);border:1px solid #fff"></div>
      <div class="abs" style="right:6px;top:6px;width:9px;height:9px;border-radius:50%;background:#fff;color:var(--red);padding:2px"><svg class="icon"><use href="#i-pencil"/></svg></div>
      <div class="abs" style="left:0;right:0;top:39px;text-align:center;font-size:4px;font-weight:600">Name Surname</div>
      <div class="abs" style="left:0;right:0;top:45px;text-align:center;font-size:3.6px;color:var(--muted)">BrightOrchard</div>
    </div>
    <div class="lbl" style="left:8px;top:72px">Impact Drive</div>
    <div class="tiles" style="left:8px;top:81px">
      <div class="tile"><svg class="icon"><use href="#i-globe"/></svg>Social Impact</div>
      <div class="tile"><svg class="icon"><use href="#i-eco"/></svg>Environmental</div>
      <div class="tile"><svg class="icon"><use href="#i-book"/></svg>Educational</div>
      <div class="tile"><svg class="icon"><use href="#i-users"/></svg>Community</div>
    </div>
    <div class="card" style="left:114px;top:18px;width:100px;height:80px;background:#eeeded">
      <div class="abs" style="left:4px;top:2px;font-size:11px;font-weight:700;line-height:.95">The Ecological<br>Guardian</div>
      <svg class="abs" style="left:6px;top:34px;width:28px;height:28px" viewBox="0 0 36 36" aria-label="Donut chart">
        <circle cx="18" cy="18" r="13" fill="none" stroke="#c9c9cb" stroke-width="7"/>
        <circle cx="18" cy="18" r="13" fill="none" stroke="#6c6c70" stroke-width="7" stroke-dasharray="40 82" transform="rotate(-90 18 18)"/>
        <circle cx="18" cy="18" r="13" fill="none" stroke="#3a3a3d" stroke-width="7" stroke-dasharray="18 82" stroke-dashoffset="-40" transform="rotate(-90 18 18)"/>
      </svg>
      <div class="abs tiny" style="left:42px;top:37px;line-height:2.9">● Ambition &amp; Skills<br>● Sustainability Alignment<br>● Community Membership &amp; Update</div>
      <div class="abs" style="left:4px;top:68px;display:flex;gap:5px;font-size:1.9px;font-weight:600">
        <span style="display:flex;gap:1px;align-items:center"><i style="width:4px;height:4px;background:var(--red);display:block"></i>Ambitions &amp; Skills</span>
        <span style="display:flex;gap:1px;align-items:center"><i style="width:4px;height:4px;background:var(--red);display:block"></i>Sustainability Alignment</span>
        <span style="display:flex;gap:1px;align-items:center"><i style="width:4px;height:4px;background:var(--red);display:block"></i>Community Membership</span>
      </div>
    </div>
    <div class="lbl" style="left:8px;top:109px">Community</div>
    <div class="tiles" style="left:8px;top:119px;gap:5px">
      <div class="ctile"><svg class="icon"><use href="#i-lock"/></svg>Security</div>
      <div class="ctile"><svg class="icon"><use href="#i-globe"/></svg>Global Impact</div>
      <div class="ctile"><svg class="icon"><use href="#i-leaf"/></svg>Eco friendly</div>
    </div>
    <div class="card" style="left:114px;top:103px;width:100px;height:70px;background:#f4f3f3">
      <div class="abs" style="left:4px;top:4px;font-size:4px">Bar Chart</div>
      <svg class="abs" style="left:2px;top:24px;width:96px;height:44px" viewBox="0 0 96 44" aria-label="Bar chart of items one to five">
        <g font-size="3" fill="#555" font-family="Poppins,sans-serif">
          <text x="1" y="4">25</text><text x="1" y="9">20</text><text x="1" y="14">15</text><text x="1" y="19">10</text><text x="2" y="25">5</text><text x="2" y="30">0</text>
        </g>
        <rect x="14" y="22" width="4" height="8" fill="#ef9aa0"/><rect x="18" y="24" width="4" height="6" fill="#888"/><rect x="22" y="22" width="4" height="8" fill="#e01722"/>
        <rect x="31" y="20" width="4" height="10" fill="#ef9aa0"/><rect x="35" y="18" width="4" height="12" fill="#e01722"/><rect x="39" y="25" width="4" height="5" fill="#888"/>
        <rect x="47" y="14" width="4" height="16" fill="#e01722"/><rect x="51" y="20" width="4" height="10" fill="#ef9aa0"/><rect x="55" y="24" width="4" height="6" fill="#888"/>
        <rect x="63" y="12" width="4" height="18" fill="#ef9aa0"/><rect x="67" y="16" width="4" height="14" fill="#e01722"/><rect x="71" y="22" width="4" height="8" fill="#888"/>
        <rect x="79" y="6" width="4" height="24" fill="#ef9aa0"/><rect x="83" y="10" width="4" height="20" fill="#e01722"/><rect x="87" y="22" width="4" height="8" fill="#888"/>
        <g font-size="3" fill="#555" font-family="Poppins,sans-serif"><text x="15" y="35">Item 1</text><text x="32" y="35">Item 2</text><text x="48" y="35">Item 3</text><text x="64" y="35">Item 4</text><text x="80" y="35">Item 5</text></g>
      </svg>
    </div>
  </div>
</section>

<!-- ============ Web: Community Insight ============ -->
<section class="desk" style="left:479px;top:403px" aria-label="Community insight dashboard">
  <aside class="side">
    <div class="brand light" style="left:9px;top:15px;font-size:6px"><span class="dot" style="width:6px;height:6px"></span>BrightOrchard</div>
    <div class="menu">
      <div class="item"><svg class="icon"><use href="#i-home"/></svg>Home</div>
      <div class="item"><svg class="icon"><use href="#i-user"/></svg>Profile</div>
      <div class="item on"><svg class="icon"><use href="#i-globe"/></svg>Community Insight</div>
      <div class="item"><svg class="icon"><use href="#i-user"/></svg>Contact Us</div>
      <div class="item"><svg class="icon"><use href="#i-gear"/></svg>Settings</div>
    </div>
    <div class="rule"></div>
    <div class="foot">
      <div class="item"><svg class="icon"><use href="#i-user"/></svg>Add Account</div>
      <div class="item"><svg class="icon"><use href="#i-swap"/></svg>Switch Account</div>
      <div class="item"><svg class="icon"><use href="#i-out"/></svg>Log Out</div>
    </div>
  </aside>
  <div class="main">
    <h2 style="top:12px">Community Insight</h2>
    <div class="tools"><svg class="icon"><use href="#i-chat"/></svg><svg class="icon" style="color:var(--red)"><use href="#i-bell"/></svg></div>
    <div class="abs" style="right:9px;top:25px;display:flex;gap:3px">
      <span style="width:7px;height:7px;border-radius:1px;background:#e2e2e4;padding:1px"><svg class="icon"><use href="#i-back"/></svg></span>
      <span style="width:7px;height:7px;border-radius:1px;background:#e2e2e4;padding:1px"><svg class="icon"><use href="#i-chev"/></svg></span>
    </div>
    <div class="card" role="img" aria-label="Dark space scene with glowing red planets" style="left:11px;top:37px;width:106px;height:67px;background:radial-gradient(circle at 50% 30%,#e8612e 0,#9d2316 16%,#3a1411 38%,#180b0b 80%)">
      <div class="abs" style="left:6px;right:6px;top:40px;text-align:center;font-size:3.2px;color:#f1d8d8;line-height:1.3">Your community is thriving! Stay<br>connected and explore new opportunities.</div>
      <div class="abs" style="left:45px;top:54px;width:17px;height:5px;border-radius:3px;background:var(--red);color:#fff;font-size:2.4px;font-weight:600;display:flex;align-items:center;justify-content:center">EXPLORE</div>
    </div>
    <div class="card" style="left:123px;top:37px;width:78px;height:67px;background:#f1f0f0">
      <svg class="abs" style="left:4px;top:5px;width:26px;height:18px" viewBox="0 0 26 18" aria-label="Line chart"><path d="M0 18H26M0 0V18" stroke="#bbb" stroke-width=".4" fill="none"/><path d="M1 14l5-6 4 4 5-7 4 3 5-6" stroke="#e01722" stroke-width=".8" fill="none"/><path d="M1 16l5-4 4 2 5-4 4 1 5-3" stroke="#ef9aa0" stroke-width=".6" fill="none"/></svg>
      <div class="abs" style="left:32px;top:6px;font-size:3.8px;font-weight:600;line-height:1">Your<br>Matches</div>
      <div class="abs tiny" style="left:32px;top:15px;width:24px;font-size:1.6px">Top match roles aligned with your values</div>
      <div class="abs" style="right:4px;top:6px;font-size:7px;font-weight:700;line-height:.9;text-align:right">85%<br><span style="font-size:4.2px">Match</span></div>
      <div class="abs" style="right:4px;top:21px;background:var(--red);color:#fff;font-size:2.2px;padding:1px 3px;border-radius:1px">View All</div>
      <div class="abs" style="left:6px;right:6px;top:32px;height:.8px;background:var(--ink)"></div>
      <svg class="abs" style="left:4px;top:38px;width:26px;height:24px" viewBox="0 0 26 24" aria-label="Bar chart"><rect x="2" y="18" width="3" height="6" fill="#999"/><rect x="7" y="14" width="3" height="10" fill="#ef9aa0"/><rect x="12" y="10" width="3" height="14" fill="#bbb"/><rect x="17" y="6" width="3" height="18" fill="#ef9aa0"/><rect x="22" y="2" width="3" height="22" fill="#e01722"/></svg>
      <div class="abs" style="left:32px;top:41px;font-size:3.8px;font-weight:600;line-height:1">Eco<br>Solutions</div>
      <div class="abs tiny" style="left:32px;top:51px;width:24px;font-size:1.6px">Start connecting and build your impact network</div>
      <div class="abs" style="right:4px;top:40px;font-size:7px;font-weight:700;line-height:.9;text-align:right">90%<br><span style="font-size:4.2px">Match</span></div>
      <div class="abs" style="right:4px;top:55px;background:var(--red);color:#fff;font-size:2.2px;padding:1px 3px;border-radius:1px">View All</div>
    </div>
    <div class="abs" style="left:130px;top:108px;display:flex;gap:3px">
      <span style="width:7px;height:7px;border-radius:1px;background:#e2e2e4;padding:1px"><svg class="icon"><use href="#i-back"/></svg></span>
      <span style="width:7px;height:7px;border-radius:1px;background:#e2e2e4;padding:1px"><svg class="icon"><use href="#i-chev"/></svg></span>
    </div>
    <div class="card" style="left:12px;top:119px;width:126px;height:50px;background:#f1eded">
      <div class="art" role="img" aria-label="Hands holding a puzzle piece" style="left:5px;top:5px;width:56px;height:36px;border-radius:2px;background:linear-gradient(135deg,#f1c8c0,#e6b2a8 50%,#d8d2cc)"></div>
      <div class="abs" style="left:62px;top:8px;font-size:3.8px;font-weight:600;color:var(--deep-red)">Explore Companies</div>
      <div class="abs tiny" style="left:64px;top:13px;width:56px;font-size:1.9px">• <b>Eco Solutions</b> – Driving sustainable innovation.<br>• <b>Verdant Works</b> – Top rated for impact.<br>Explore all companies to find your next partnership.</div>
      <div class="abs" style="left:91px;top:34px;background:var(--red);color:#fff;font-size:3px;padding:1.5px 5px;border-radius:2px;font-weight:600">View All</div>
    </div>
    <div class="card" style="left:143px;top:108px;width:61px;height:61px;background:linear-gradient(180deg,#c89aa0,#f3dfe1 60%,#fff)">
      <div class="abs" style="left:4px;top:5px;background:#fff;font-size:2px;padding:1px 3px;border-radius:3px;font-weight:600">Special for you!</div>
      <div class="abs" style="left:4px;top:15px;font-size:8px;font-weight:700;color:#5a1a20;line-height:1">Join Our<br>Community</div>
      <div class="abs" style="right:4px;top:43px;background:#fff;font-size:2px;padding:1px 3px;border-radius:3px;font-weight:600">Get Started ●</div>
    </div>
  </div>
</section>

<!-- ============ App: Welcome ============ -->
<section class="phone" style="left:66px;top:743px;background:var(--white)" aria-label="App welcome screen">
  <div class="status"><span>07:00 AM</span><span class="sys"><i style="width:3px;height:3px;border-radius:50%"></i><i style="width:3px;height:3px"></i><i style="width:5px;height:2.5px"></i></span></div>
  <div class="abs" style="left:61px;top:25px;width:21px;height:21px;border-radius:50%;background:var(--red)"></div>
  <div class="abs" style="left:0;right:0;top:50px;text-align:center;font-size:6.6px;font-weight:700">BrightOrchard</div>
  <div class="abs" style="right:12px;top:30px;display:flex;gap:3px;width:13px;height:5px"><svg class="icon"><use href="#i-bell"/></svg><svg class="icon"><use href="#i-menu"/></svg></div>
  <div class="art" role="img" aria-label="3D planet orbit system with satellite above a glowing red podium" style="left:14px;top:78px;width:115px;height:150px;border-radius:40px;background:radial-gradient(ellipse at 48% 30%,#ede2f6 0,#cdb9eb 28%,transparent 50%),radial-gradient(ellipse at 50% 85%,#d71a22 0,#f4958f 28%,transparent 58%)"></div>
  <div class="abs" style="left:0;right:0;top:228px;text-align:center;font-size:7.4px;font-weight:600;line-height:1.15">Discover Your<br>Sustainable Career Path<br>&amp; Make an Impact!</div>
  <div class="abs" style="left:25px;top:262px;width:93px;height:16px;border-radius:9px;background:var(--red);border:1px solid var(--deep-red);color:#fff;font-size:6.8px;font-weight:600;display:flex;align-items:center;justify-content:center">START NOW</div>
  <div class="homebar"></div>
</section>

<!-- ============ App: Our Mission ============ -->
<section class="phone" style="left:264px;top:743px;background:#fbf3f4" aria-label="Our mission screen">
  <div class="status"><span>07:00 AM</span><span class="sys"><i style="width:3px;height:3px;border-radius:50%"></i><i style="width:3px;height:3px"></i><i style="width:5px;height:2.5px"></i></span></div>
  <div class="abs" style="left:8px;top:30px;width:5px;height:5px"><svg class="icon"><use href="#i-back"/></svg></div>
  <div class="abs" style="left:61px;top:25px;width:21px;height:21px;border-radius:50%;background:var(--red)"></div>
  <div class="abs" style="right:12px;top:30px;display:flex;gap:3px;width:13px;height:5px"><svg class="icon"><use href="#i-bell"/></svg><svg class="icon"><use href="#i-menu"/></svg></div>
  <div class="abs" style="left:0;right:0;top:47px;text-align:center;font-size:7.8px;font-weight:700">Our Mission</div>
  <div class="art" role="img" aria-label="3D globe wrapped in a red geodesic network" style="left:4px;top:62px;width:135px;height:135px;border-radius:50%;background:radial-gradient(circle at 48% 45%,#f4f4f4 0,#d9d9d9 30%,#c63a3c 50%,#f3c2c4 66%,transparent 70%)"></div>
  <div class="art" role="img" aria-label="Red data network lines" style="left:0;top:195px;width:143px;height:60px;background:linear-gradient(180deg,rgba(220,60,70,.18),transparent)"></div>
  <div class="abs" style="left:0;right:0;top:262px;text-align:center;font-size:5.6px;font-weight:600;line-height:1.2">We connect young<br>professionals with purposeful<br>work in sustainable<br>companies.</div>
  <div class="homebar"></div>
</section>

<!-- ============ App: Profile ============ -->
<section class="phone" style="left:461px;top:743px;background:#ece8e8" aria-label="App profile screen">
  <div class="abs" role="img" aria-label="Soft pink space backdrop" style="left:0;top:0;width:143px;height:78px;background:linear-gradient(180deg,#b38c90,#d9b4b8)"></div>
  <div class="abs" style="left:0;top:68px;width:143px;height:60px;border-radius:14px 14px 0 0;background:#ece8e8"></div>
  <div class="status" style="color:#fff"><span>07:00 AM</span><span class="sys"><i style="width:3px;height:3px;border-radius:50%"></i><i style="width:3px;height:3px"></i><i style="width:5px;height:2.5px"></i></span></div>
  <div class="abs" style="left:10px;top:18px;width:6px;height:6px;color:#fff"><svg class="icon"><use href="#i-menu"/></svg></div>
  <div class="abs" style="left:0;right:0;top:18px;text-align:center;font-size:8.5px;color:#fff">Profile</div>
  <div class="abs" style="right:12px;top:17px;width:10px;height:10px;border-radius:50%;background:#fff;color:var(--red);padding:2px"><svg class="icon"><use href="#i-pencil"/></svg></div>
  <div class="art" role="img" aria-label="Member portrait" style="left:44px;top:44px;width:55px;height:55px;border-radius:50%;background:radial-gradient(circle,#7a5646,#2c1e1a);border:1.5px solid #fff"></div>
  <div class="abs" style="left:0;right:0;top:103px;text-align:center;font-size:5.2px;font-weight:600">Name Surname</div>
  <div class="abs" style="left:0;right:0;top:111px;text-align:center;font-size:4.6px;color:var(--muted)">BrightOrchard</div>
  <div class="abs" style="left:5px;top:122px;width:133px;height:54px;border-radius:6px;background:linear-gradient(180deg,#3a1e1f,#c9a4a7 80%,#ece8e8)"></div>
  <div class="abs" style="left:10px;top:128px;font-size:6.4px;color:#fff">Impact Drive</div>
  <div class="tiles" style="left:12px;top:143px;gap:3px">
    <div class="tile" style="width:27px;height:24px"><svg class="icon"><use href="#i-globe"/></svg>Social Impact</div>
    <div class="tile" style="width:27px;height:24px"><svg class="icon"><use href="#i-eco"/></svg>Environmental</div>
    <div class="tile" style="width:27px;height:24px"><svg class="icon"><use href="#i-book"/></svg>Educational</div>
    <div class="tile" style="width:27px;height:24px"><svg class="icon"><use href="#i-users"/></svg>Community</div>
  </div>
  <div class="abs" style="left:9px;top:179px;font-size:6.4px">Learning Goals</div>
  <div class="abs" style="left:7px;top:189px;width:129px;height:40px;border-radius:3px;background:#fff"></div>
  <div class="row" style="top:192px"><span class="ic"><svg class="icon"><use href="#i-target"/></svg></span>Target<svg class="icon chev"><use href="#i-chev"/></svg></div>
  <div class="row" style="top:208px;border:none"><span class="ic"><svg class="icon"><use href="#i-target"/></svg></span>Goals<svg class="icon chev"><use href="#i-chev"/></svg></div>
  <div class="abs" style="left:9px;top:233px;font-size:6.4px">Community</div>
  <div class="abs" style="left:7px;top:243px;width:129px;height:52px;border-radius:3px;background:#fff"></div>
  <div class="row" style="top:245px"><span class="ic"><svg class="icon"><use href="#i-lock"/></svg></span>Security<svg class="icon chev"><use href="#i-chev"/></svg></div>
  <div class="row" style="top:261px"><span class="ic"><svg class="icon"><use href="#i-globe"/></svg></span>Global Impact<svg class="icon chev"><use href="#i-chev"/></svg></div>
  <div class="row" style="top:277px;border:none"><span class="ic"><svg class="icon"><use href="#i-leaf"/></svg></span>Eco Friendly<svg class="icon chev"><use href="#i-chev"/></svg></div>
</section>

<!-- ============ App: Community Insight ============ -->
<section class="phone" style="left:658px;top:743px;background:#fbf6f6" aria-label="App community insight screen">
  <div class="status"><span>07:00 AM</span><span class="sys"><i style="width:3px;height:3px;border-radius:50%"></i><i style="width:3px;height:3px"></i><i style="width:5px;height:2.5px"></i></span></div>
  <div class="abs" style="left:10px;top:18px;width:6px;height:6px"><svg class="icon"><use href="#i-menu"/></svg></div>
  <div class="brand" style="left:48px;top:17px;font-size:6.8px"><span class="dot" style="width:6px;height:6px"></span>BrightOrchard</div>
  <div class="art" role="img" aria-label="Member avatar" style="right:9px;top:16px;width:10px;height:10px;border-radius:50%;background:radial-gradient(circle,#7a5646,#2c1e1a)"></div>
  <div class="abs" role="img" aria-label="Dark space scene with glowing red planets" style="left:10px;top:26px;width:124px;height:75px;border-radius:4px;background:radial-gradient(circle at 50% 20%,#ec6a2f 0,#a52617 16%,#3b1412 40%,#170a0a 85%)"></div>
  <div class="abs" style="left:10px;top:43px;width:124px;text-align:center;font-family:'DM Serif Display',serif;font-size:13.5px;line-height:.95;color:#fff">Community<br>Insight</div>
  <div class="abs" style="left:10px;top:72px;width:124px;text-align:center;font-size:3.6px;color:#f1d8d8;line-height:1.3">Your community is thriving! Stay connected<br>and explore new opportunities.</div>
  <div class="abs" style="left:61px;top:86px;width:22px;height:6px;border-radius:3px;background:var(--red);color:#fff;font-size:2.8px;font-weight:600;display:flex;align-items:center;justify-content:center">EXPLORE</div>
  <div class="abs" style="left:9px;top:108px;width:125px;height:10px;border-radius:5px;background:#fff;border:.5px solid var(--line);font-size:3.6px;color:#999;padding-left:16px;display:flex;align-items:center">Search your favorite solutions....</div>
  <div class="abs" style="left:9px;top:108px;width:10px;height:10px;border-radius:50%;background:#888;color:#fff;padding:2.5px"><svg class="icon"><use href="#i-menu"/></svg></div>
  <div class="abs" style="right:12px;top:110px;width:6px;height:6px"><svg class="icon"><use href="#i-search"/></svg></div>
  <div class="match" style="top:126px;height:38px">
    <div class="art" role="img" aria-label="Hands holding a puzzle piece" style="left:3px;top:4px;width:50px;height:30px;border-radius:2px;background:linear-gradient(135deg,#f1c8c0,#e6b2a8 50%,#d8d2cc)"></div>
    <div class="abs" style="left:59px;top:4px;font-size:4.2px;font-weight:600;color:var(--deep-red)">Explore Companies</div>
    <div class="abs tiny" style="left:60px;top:9px;width:60px;font-size:2.2px">• <b>Eco Solutions</b> – Driving sustainable innovation.<br>• <b>Verdant Works</b> – Top rated for impact.<br>Explore all companies to find your next partnership.</div>
    <div class="go" style="font-size:2.6px">View All</div>
  </div>
  <div class="match" style="top:172px">
    <svg class="abs" style="left:4px;top:5px;width:40px;height:32px" viewBox="0 0 40 32" aria-label="Line chart"><path d="M2 30H40M2 0V30" stroke="#bbb" stroke-width=".5" fill="none"/><path d="M3 24l7-10 6 7 7-12 6 5 8-12" stroke="#e01722" stroke-width=".9" fill="none"/><path d="M3 27l7-6 6 3 7-7 6 2 8-5" stroke="#ef9aa0" stroke-width=".7" fill="none"/></svg>
    <div class="ttl">Your<br>Matches</div>
    <div class="abs tiny" style="left:48px;top:22px;width:36px;font-size:1.8px">Top roles aligned with your values and skills this week</div>
    <div class="pct">85%<small>Match</small></div>
    <div class="go">View All</div>
  </div>
  <div class="match" style="top:220px">
    <svg class="abs" style="left:6px;top:5px;width:36px;height:32px" viewBox="0 0 36 32" aria-label="Bar chart"><rect x="3" y="24" width="4" height="8" fill="#999"/><rect x="9" y="18" width="4" height="14" fill="#ef9aa0"/><rect x="15" y="14" width="4" height="18" fill="#bbb"/><rect x="21" y="8" width="4" height="24" fill="#ef9aa0"/><rect x="27" y="3" width="4" height="29" fill="#e01722"/></svg>
    <div class="ttl">Eco<br>Solutions</div>
    <div class="abs tiny" style="left:48px;top:22px;width:36px;font-size:1.8px;font-style:italic">Start connecting and build your impact network</div>
    <div class="pct">90%<small>Match</small></div>
    <div class="go">View All</div>
  </div>
  <div class="abs" style="left:11px;top:276px;display:flex;gap:2px;align-items:center"><i style="display:block;width:9px;height:2px;border-radius:1px;background:var(--red)"></i><i style="display:block;width:3px;height:2px;border-radius:1px;background:#ccc"></i><i style="display:block;width:3px;height:2px;border-radius:1px;background:#ccc"></i><i style="display:block;width:3px;height:2px;border-radius:1px;background:#ccc"></i></div>
  <div class="abs" style="right:10px;top:274px;font-size:3.8px">See More ›</div>
  <div class="abs" style="left:9px;top:285px;width:54px;height:13px;border-radius:7px;background:var(--red);color:#fff;font-size:4.4px;font-weight:600;display:flex;align-items:center;gap:5px;padding-left:2px">
    <span style="width:10px;height:10px;border-radius:50%;background:#fff;color:var(--red);padding:2px"><svg class="icon"><use href="#i-home"/></svg></span>DASHBOARD
  </div>
  <div class="abs" style="left:74px;top:288px;display:flex;gap:9px;color:var(--muted)">
    <span style="width:7px;height:7px"><svg class="icon"><use href="#i-compass"/></svg></span>
    <span style="width:7px;height:7px"><svg class="icon"><use href="#i-heart"/></svg></span>
    <span style="width:7px;height:7px"><svg class="icon"><use href="#i-chat"/></svg></span>
    <span style="width:7px;height:7px"><svg class="icon"><use href="#i-user"/></svg></span>
  </div>
</section>

</body>
</html>
```